Elm Ridge Baptist Church sign

We want a colourful, attractive sign that includes connection to being a Christian Church living in the foothills of the Canadian Rocky Mountains. As far as printed words, we need it to say “ Elm Ridge Baptist Church”. We are planning on a sign that is 6’ x 4’. Our church slogan is:
“ Live like Jesus, Love like Jesus”. This slogan could be included on the sign if space allows. To all designers; in talking with the communications team at our church, we want to eliminate the church’s slogan “ live like Jesus, live like Jesus “, from being on the sign.

```html
<!DOCTYPE html>
<html lang="en">
<head>
<meta charset="UTF-8">
<title>Elm Ridge Baptist Church Sign</title>
<link href="https://fonts.googleapis.com/css2?family=Allura&family=Kaushan+Script&display=swap" rel="stylesheet">
<style>
  :root {
    --page: #ffffff;
    --sky-deep: #0a78c4;
    --sky-mid: #3aa6e6;
    --sky-light: #8fd0f4;
    --cloud: #f4fbff;
    --mountain: #7fc3e6;
    --haze: #4aa3cf;
    --field: #3f9a48;
    --forest: #163f2a;
    --forest-deep: #0c2a1c;
    --name-blue: #1a5d8c;
    --subtitle: #ffffff;
  }
  * { margin: 0; padding: 0; box-sizing: border-box; }
  html, body {
    width: 1200px;
    height: 1200px;
    overflow: hidden;
    background: var(--page);
  }
  .canvas {
    position: relative;
    width: 1200px;
    height: 1200px;
    background: var(--page);
  }
  .sign {
    position: absolute;
    left: 150px;
    top: 300px;
    width: 900px;
    height: 600px;
    overflow: hidden;
  }
  .sign__scene {
    position: absolute;
    inset: 0;
    background:
      radial-gradient(ellipse 330px 190px at 470px 330px, rgba(255,255,255,0.95), rgba(255,255,255,0) 100%),
      linear-gradient(180deg,
        var(--sky-deep) 0%,
        var(--sky-mid) 22%,
        var(--sky-light) 38%,
        var(--cloud) 50%,
        var(--cloud) 55%,
        var(--mountain) 60%,
        var(--haze) 68%,
        var(--field) 76%,
        var(--forest) 86%,
        var(--forest-deep) 100%);
  }
  .sign__name {
    position: absolute;
    left: 0;
    width: 100%;
    top: 100px;
    text-align: center;
    white-space: nowrap;
    font-family: "Allura", cursive;
    font-weight: 400;
    font-size: 220px;
    line-height: 1;
    color: var(--name-blue);
  }
  .sign__subtitle {
    position: absolute;
    left: 0;
    width: 100%;
    top: 372px;
    text-align: center;
    white-space: nowrap;
    font-family: "Kaushan Script", cursive;
    font-weight: 400;
    font-size: 92px;
    line-height: 1;
    color: var(--subtitle);
  }
</style>
</head>
<body>
  <main class="canvas">
    <section class="sign">
      <div class="sign__scene" role="img" aria-label="Landscape of blue sky with bright clouds above snow-capped Rocky Mountain peaks, green foothill fields and dark forest"></div>
      <h1 class="sign__name">Elm Ridge</h1>
      <p class="sign__subtitle">Baptist Church</p>
    </section>
  </main>
</body>
</html>
```